Tavo Payments Business card refresh

Need a new design of our business card The info is not what is on these cards i sent this for a reference. I can email all the info over
Info would be Derek Whitfield Chief TAVO is the title. our new address is 47615 Birch Hollow Rd. Cedar Ridge Ca 91384 Cell number is 805-634-2917 Work number is 855-482-7309 ext 347 Derek@tavopayments.com is my email address
Target Market(s)
Merchant Services all businesses that take credit cards
Industry/Entity Type
Merchant Services / Credit Card processing
Contact Information for Business Card
Need a new design of our business card The info is not what is on these cards i sent this for a reference. I can email all the info over Info would be Derek Whitfield Chief TAVO is the title. our new address is 47615 Birch Hollow Rd. Cedar Ridge Ca 91384 Cell number is 805-634-2917 Work number is 855-482-7309 ext 347 Derek@tavopayments.com is my email address
Requirements
Must have
- My logo and colors from my brand guidelines
Nice to have
- i sent some designs just need a new refresh
Should not have
- nothing specific

```html
<!DOCTYPE html>
<html lang="en">
<head>
<meta charset="utf-8">
<title>Tavo Payments – Business Card</title>
<link href="https://fonts.googleapis.com/css2?family=Lato:wght@400;700;900&display=swap" rel="stylesheet">
<style>
  :root {
    --stage: #1d1e20;
    --lime: #95c11f;
    --charcoal: #2a2d31;
    --ink: #26292d;
    --white: #ffffff;
    --muted: #e9ecef;
  }
  * { margin: 0; padding: 0; box-sizing: border-box; }
  html, body {
    width: 1200px;
    height: 875px;
    overflow: hidden;
    background: var(--stage);
    font-family: "Lato", sans-serif;
  }
  .canvas {
    position: relative;
    width: 1200px;
    height: 875px;
  }
  .card {
    position: absolute;
    width: 560px;
    height: 320px;
    border-radius: 4px;
    overflow: hidden;
  }
  .card--front {
    left: 70px;
    top: 100px;
    background: var(--lime);
    display: flex;
    align-items: center;
    justify-content: center;
  }
  .card--back {
    left: 570px;
    top: 455px;
    background: var(--charcoal);
  }

  .wordmark {
    display: flex;
    flex-direction: column;
    align-items: flex-start;
    font-weight: 900;
    line-height: 1;
  }
  .wordmark__name {
    font-size: 96px;
    letter-spacing: 2px;
  }
  .wordmark__sub {
    font-size: 22px;
    letter-spacing: 15px;
    margin-top: 4px;
    margin-left: 48px;
  }
  .card--front .wordmark { color: var(--ink); }

  .card--back .wordmark {
    position: absolute;
    left: 34px;
    top: 40px;
    color: var(--white);
  }
  .card--back .wordmark__name { font-size: 64px; }
  .card--back .wordmark__sub {
    font-size: 15px;
    letter-spacing: 10px;
    margin-left: 32px;
  }

  .contact-list {
    position: absolute;
    left: 40px;
    top: 158px;
    list-style: none;
    color: var(--white);
    font-size: 14px;
    line-height: 1.45;
  }
  .contact-list li {
    display: flex;
    align-items: flex-start;
    gap: 9px;
  }
  .contact-list .is-strong { font-weight: 700; font-size: 16px; }
  .contact-list svg {
    flex: none;
    width: 13px;
    height: 13px;
    margin-top: 4px;
    fill: none;
    stroke: var(--lime);
    stroke-width: 2;
    stroke-linecap: round;
    stroke-linejoin: round;
  }

  .person {
    position: absolute;
    right: 30px;
    top: 120px;
    text-align: right;
  }
  .person__name {
    color: var(--lime);
    font-weight: 900;
    font-size: 26px;
    letter-spacing: 0.5px;
  }
  .person__title {
    color: var(--muted);
    font-weight: 400;
    font-size: 16px;
    margin-top: 2px;
  }
</style>
</head>
<body>
<main class="canvas">

  <section class="card card--front" aria-label="Card front">
    <div class="wordmark">
      <span class="wordmark__name">TAVO</span>
      <span class="wordmark__sub">PAYMENTS</span>
    </div>
  </section>

  <section class="card card--back" aria-label="Card back">
    <div class="wordmark">
      <span class="wordmark__name">TAVO</span>
      <span class="wordmark__sub">PAYMENTS</span>
    </div>

    <ul class="contact-list">
      <li class="is-strong">
        <svg viewBox="0 0 16 16" aria-hidden="true"><path d="M3 2h3l1.5 3.5-2 1.2a8 8 0 0 0 3.8 3.8l1.2-2L14 10v3a1 1 0 0 1-1 1A11 11 0 0 1 2 3a1 1 0 0 1 1-1z"/></svg>
        <span>855-482-7309 ext 347</span>
      </li>
      <li class="is-strong">
        <svg viewBox="0 0 16 16" aria-hidden="true"><rect x="4" y="1.5" width="8" height="13" rx="1.5"/><path d="M7 12.2h2"/></svg>
        <span>805-634-2917</span>
      </li>
      <li>
        <svg viewBox="0 0 16 16" aria-hidden="true"><rect x="1.5" y="3.5" width="13" height="9" rx="1"/><path d="M2 4l6 5 6-5"/></svg>
        <span>Derek@tavopayments.com</span>
      </li>
      <li>
        <svg viewBox="0 0 16 16" aria-hidden="true"><circle cx="8" cy="8" r="6.5"/><path d="M1.5 8h13M8 1.5c2.2 2 2.2 11 0 13M8 1.5c-2.2 2-2.2 11 0 13"/></svg>
        <span>tavopayments.com</span>
      </li>
      <li>
        <svg viewBox="0 0 16 16" aria-hidden="true"><path d="M8 15s5-5 5-8.5A5 5 0 0 0 3 6.5C3 10 8 15 8 15z"/><circle cx="8" cy="6.5" r="1.8"/></svg>
        <span>47615 Birch Hollow Rd.<br>Cedar Ridge Ca 91384</span>
      </li>
    </ul>

    <div class="person">
      <p class="person__name">DEREK WHITFIELD</p>
      <p class="person__title">Chief TAVO</p>
    </div>
  </section>

</main>
</body>
</html>
```